Psychologist Banner Ads for Remarketing & yarnwave

Brand awareness campaign for tallowbridge.com.au

// Ad Formats //
Static JPEG
Max 45KB in file size
All ads must have a border

// Ad Sizes //
Static: (for Zindle Display network) 300×250, 160×600, 728×90
Static: (for Yarnwave, no more than 25% text): 600×315, 1200 x 627

Please use logo, image and "maximise your wellbeing" from the website home page.

```html
<!DOCTYPE html>
<html lang="en">
<head>
<meta charset="utf-8">
<title>Tallowbridge Psychology – Maximise Your Wellbeing banner set</title>
<link rel="stylesheet" href="https://fonts.googleapis.com/css2?family=Ultra&family=Arimo:wght@400&display=swap">
<style>
  :root {
    --brand-blue: #0d9ccf;
    --deep-navy: #17408f;
    --tagline-blue: #1f4fa3;
    --sky-top: #bfe3f5;
    --sky-bottom: #f4f8fb;
    --photo-warm: #d9b8a0;
    --paper: #ffffff;
    --frame: #0a0a0a;
    --stage: #eef1f4;
  }
  * { box-sizing: border-box; margin: 0; padding: 0; }
  html, body { width: 1200px; height: 900px; overflow: hidden; background: var(--stage); }
  .canvas { position: relative; width: 1200px; height: 900px; }

  .ad { position: absolute; background: var(--paper); border: 4px solid var(--frame); overflow: hidden; }
  .ad svg { position: absolute; inset: 0; width: 100%; height: 100%; display: block; }
  .ad-leaderboard { left: 141px; top: 53px; width: 851px; height: 102px; }
  .ad-rectangle   { left: 246px; top: 334px; width: 391px; height: 324px; }
  .ad-skyscraper  { left: 805px; top: 176px; width: 186px; height: 700px; }

  .headline { position: absolute; font-family: "Ultra", "Rockwell", serif; font-weight: 400; color: var(--paper); line-height: 1; letter-spacing: 0.5px; white-space: nowrap; }
  .tagline { position: absolute; font-family: "Arimo", Arial, sans-serif; color: var(--tagline-blue); line-height: 1.15; white-space: nowrap; }

  .brand { position: absolute; font-family: "Arimo", Arial, sans-serif; font-weight: 400; color: var(--deep-navy); line-height: 1; text-align: left; white-space: nowrap; }
  .brand-name { display: block; }
  .brand-field { display: block; letter-spacing: 2px; text-transform: uppercase; margin-top: 4px; }

  /* leaderboard */
  .ad-leaderboard .headline { left: 16px; top: 14px; font-size: 34px; }
  .ad-leaderboard .tagline { left: 56px; top: 52px; font-size: 22px; }
  .ad-leaderboard .brand { right: 26px; top: 24px; }
  .ad-leaderboard .brand-name { font-size: 27px; }
  .ad-leaderboard .brand-field { font-size: 13px; }

  /* rectangle */
  .ad-rectangle .headline { right: 8px; top: 24px; font-size: 36px; }
  .ad-rectangle .tagline { right: 44px; top: 62px; font-size: 23px; }
  .ad-rectangle .brand { right: 10px; bottom: 14px; }
  .ad-rectangle .brand-name { font-size: 27px; }
  .ad-rectangle .brand-field { font-size: 15px; }

  /* skyscraper */
  .ad-skyscraper .headline { left: 0; right: 0; top: 66px; font-size: 23px; text-align: center; }
  .ad-skyscraper .tagline { left: 0; right: 0; top: 100px; font-size: 29px; text-align: center; line-height: 1.35; }
  .ad-skyscraper .brand { left: 16px; bottom: 30px; }
  .ad-skyscraper .brand-name { font-size: 26px; }
  .ad-skyscraper .brand-field { font-size: 14px; }
</style>
</head>
<body>
<main class="canvas">

  <!-- 728 x 90 leaderboard -->
  <section class="ad ad-leaderboard" aria-label="Leaderboard banner">
    <svg viewBox="0 0 843 94" preserveAspectRatio="none">
      <defs>
        <linearGradient id="sky-lb" x1="0" y1="0" x2="0" y2="1">
          <stop offset="0" stop-color="var(--sky-top)"/>
          <stop offset="0.7" stop-color="var(--sky-bottom)"/>
          <stop offset="1" stop-color="var(--photo-warm)"/>
        </linearGradient>
      </defs>
      <rect class="band" x="0" y="0" width="340" height="94" fill="var(--brand-blue)"/>
      <ellipse class="photo" role="img" aria-label="Photo of a smiling woman raising her arms to the sky"
               cx="458" cy="40" rx="158" ry="200" fill="url(#sky-lb)" stroke="var(--deep-navy)" stroke-width="4"/>
    </svg>
    <h2 class="headline">MAXIMISE</h2>
    <p class="tagline">Your Wellbeing</p>
    <p class="brand"><span class="brand-name">Tallowbridge</span><span class="brand-field">Psychology</span></p>
  </section>

  <!-- 300 x 250 medium rectangle -->
  <section class="ad ad-rectangle" aria-label="Medium rectangle banner">
    <svg viewBox="0 0 383 316">
      <defs>
        <linearGradient id="sky-rect" x1="0" y1="0" x2="0" y2="1">
          <stop offset="0" stop-color="var(--sky-top)"/>
          <stop offset="0.65" stop-color="var(--sky-bottom)"/>
          <stop offset="1" stop-color="var(--photo-warm)"/>
        </linearGradient>
      </defs>
      <path class="band" d="M0 0 H383 V198 Q320 246 200 252 L0 252 Z" fill="var(--brand-blue)"/>
      <path class="band-edge" d="M383 198 Q320 246 200 252" fill="none" stroke="var(--deep-navy)" stroke-width="4"/>
      <circle class="photo" role="img" aria-label="Photo of a smiling woman raising her arms to the sky"
              cx="108" cy="182" r="112" fill="url(#sky-rect)" stroke="var(--deep-navy)" stroke-width="4"/>
    </svg>
    <h2 class="headline">MAXIMISE</h2>
    <p class="tagline">Your Wellbeing</p>
    <p class="brand"><span class="brand-name">Tallowbridge</span><span class="brand-field">Psychology</span></p>
  </section>

  <!-- 160 x 600 skyscraper -->
  <section class="ad ad-skyscraper" aria-label="Skyscraper banner">
    <svg viewBox="0 0 178 692">
      <defs>
        <linearGradient id="sky-sky" x1="0" y1="0" x2="0" y2="1">
          <stop offset="0" stop-color="var(--sky-top)"/>
          <stop offset="0.6" stop-color="var(--sky-bottom)"/>
          <stop offset="1" stop-color="var(--photo-warm)"/>
        </linearGradient>
      </defs>
      <rect class="band" x="0" y="0" width="178" height="370" fill="var(--brand-blue)"/>
      <ellipse class="photo" role="img" aria-label="Photo of a smiling woman raising her arms to the sky"
               cx="89" cy="367" rx="180" ry="164" fill="url(#sky-sky)" stroke="var(--deep-navy)" stroke-width="4"/>
      <rect class="lower-panel" x="0" y="533" width="178" height="159" fill="var(--paper)"/>
    </svg>
    <h2 class="headline">MAXIMISE</h2>
    <p class="tagline">Your<br>Wellbeing</p>
    <p class="brand"><span class="brand-name">Tallowbridge</span><span class="brand-field">Psychology</span></p>
  </section>

</main>
</body>
</html>
```